I need a business card design for my new clinic (ATHLETIC CARE OF JOINT). I am orthopedist, expert in sports surgery, especially knee surgery. I prefer, as colors, the colors of my logo (green, black and white). I already have my logo and should appear on my card. It's good to see my site to have ideas (www.drlucianovarela.example)
It needs contain:
my name: Dr. Luciano Varela
my registration: CRM 584-902
my specialty: Cirurgia do Joelho / Esporte
my address: Centro Empresarial - Parque Aurora Mall
Av. Doutor Augusto Valadares Pinto, 2740 sala 803
Jd. Acácias - Ribeirão Preto - SP
my phone number: Tel (16) 8420-5937
my clinic phone: (16) 3745-8081
my e-mail: drlucianovarela@mailbox.example
my site: www.drlucianovarela.example

Target Market(s)

futures patients

Industry/Entity Type

Clinic

Requirements
Nice to have
• letters not overfilled
straight lines, with few curves

```html
<!DOCTYPE html>
<html lang="pt-BR">
<head>
<meta charset="utf-8">
<title>Athletic Care of Joint – Cartão de visita</title>
<link rel="stylesheet" href="https://fonts.googleapis.com/css2?family=Cinzel:wght@400;600&family=Montserrat:wght@500;700&display=swap">
<style>
  :root{
    --stage:#1c1c1c;
    --page:#ffffff;
    --concrete-1:#9a9a9a;
    --concrete-2:#7c7c7c;
    --ink:#0d0d0d;
    --green:#3dbb78;
    --green-dark:#1f9a5a;
    --text-grey:#6b6b6b;
    --white:#ffffff;
  }
  *{margin:0;padding:0;box-sizing:border-box}
  html,body{width:1200px;height:901px;overflow:hidden;background:var(--page)}
  .stage{position:absolute;left:50px;top:0;width:1100px;height:850px;background:var(--stage)}
  .card{position:absolute;width:538px;height:306px;background:var(--white);overflow:hidden;
        box-shadow:0 22px 26px -12px rgba(0,0,0,.7)}
  .concrete{position:absolute;left:0;right:0;
        background:linear-gradient(180deg,var(--concrete-1),var(--concrete-2))}

  /* front */
  .card--front{left:276px;top:53px}
  .front__top{top:0;height:76px}
  .front__bottom{top:232px;height:74px}
  .front__brand{position:absolute;left:18px;top:76px;height:156px;display:flex;align-items:center;gap:18px}
  .brand-square{width:124px;height:120px;background:var(--green);border:4px solid var(--ink);border-radius:10px}
  .brand-name{font-family:"Cinzel",serif;font-weight:600;font-size:80px;line-height:1;color:var(--ink);letter-spacing:1px}
  .brand-tagline{position:absolute;left:180px;top:178px;font-family:"Cinzel",serif;font-size:21px;color:var(--green-dark);letter-spacing:1px}
  .front__site{position:absolute;left:0;right:0;top:264px;text-align:center;font-family:"Cinzel",serif;
        font-size:19px;color:var(--white);letter-spacing:.5px;text-shadow:0 1px 2px rgba(0,0,0,.5)}

  /* back */
  .card--back{left:278px;top:470px}
  .back__band{top:0;height:131px}
  .stripe{position:absolute;top:0;bottom:0;width:9px;
        background:linear-gradient(180deg,var(--green) 0%,var(--green) 45%,rgba(61,187,120,0) 100%)}
  .stripe--a{left:14px}
  .stripe--b{left:31px}
  .back__mark{position:absolute;left:14px;top:22px;width:108px;height:100px;background:var(--green);
        border:4px solid var(--ink);border-radius:9px}
  .back__id{position:absolute;right:14px;top:24px;text-align:right;font-family:"Cinzel",serif;color:var(--white);
        text-shadow:0 1px 3px rgba(0,0,0,.6)}
  .id__name{font-size:29px;line-height:1.1}
  .id__crm{font-size:17px;line-height:1.3}
  .id__spec{font-size:21px;line-height:1.6;margin-top:2px}
  .back__contact{position:absolute;left:0;right:0;top:160px;text-align:center;font-family:"Montserrat",sans-serif;
        font-size:15px;line-height:20.6px;color:var(--text-grey);font-weight:500}
  .back__contact strong{font-weight:700}
  .contact__mail{color:var(--green-dark)}
</style>
</head>
<body>
<div class="stage">
  <section class="card card--front" aria-label="Frente do cartão">
    <div class="concrete front__top"></div>
    <div class="front__brand">
      <div class="brand-square"></div>
      <div class="brand-name">VARELA</div>
    </div>
    <div class="brand-tagline">Traumatologia Esportiva</div>
    <div class="concrete front__bottom"></div>
    <div class="front__site">WWW.DRLUCIANOVARELA.EXAMPLE</div>
  </section>

  <section class="card card--back" aria-label="Verso do cartão">
    <div class="concrete back__band"></div>
    <div class="stripe stripe--a"></div>
    <div class="stripe stripe--b"></div>
    <div class="back__mark"></div>
    <div class="back__id">
      <div class="id__name">Dr. Luciano Varela</div>
      <div class="id__crm">CRM 584-902</div>
      <div class="id__spec">Cirurgia do Joelho / Esporte</div>
    </div>
    <div class="back__contact">
      <strong>Centro Empresarial - Parque Aurora Mall</strong><br>
      Av. Doutor Augusto Valadares Pinto, 2740 sala 803<br>
      Jd. Acácias - Ribeirão Preto - SP<br>
      <strong>Tel (16) 8420-5937</strong><br>
      <strong>Clinic (16) 3745-8081</strong><br>
      <span class="contact__mail">drlucianovarela@mailbox.example</span>
    </div>
  </section>
</div>
</body>
</html>
```